Re-design / re-work of existing website

Need to re-design a website so it's easy for me as a user to update/add pictures and change descriptions.

If possible, would there be a way to display LodgeVista calendars? We have 3 cottages and it would be ideal to have each cottage with pics on one page along with a readonly version of the LodgeVista calendar plugin (if such a thing exists) so that visitors to the site can see what is available and what is not.

Existing site: http://tarnwoodlets.net

```html
<!DOCTYPE html>
<html lang="en">
<head>
<meta charset="utf-8">
<title>Tarnwood Cottages</title>
<link rel="stylesheet" href="https://fonts.googleapis.com/css2?family=Open+Sans:wght@400;600;700&family=Roboto:wght@400;500;700&display=swap">
<style>
:root{
  --tan:#c2ab8e;
  --tan-deep:#b89e7e;
  --tan-veil:rgba(196,170,138,.82);
  --ink:#111;
  --text:#4a4a4a;
  --white:#fff;
  --sky-top:#1d4fa8;
  --sky-low:#5b8fd6;
  --forest:#2f5a3a;
  --black:#000;
}
*{box-sizing:border-box;margin:0;padding:0}
html,body{width:1200px;height:4277px;overflow:hidden}
body{position:relative;background:var(--white);font-family:"Open Sans",sans-serif;color:var(--ink)}
.abs{position:absolute}
.photo{position:absolute;overflow:hidden}
.center{left:0;width:1200px;text-align:center}

/* buttons */
.btn{position:absolute;display:flex;align-items:center;justify-content:center;background:var(--tan);color:var(--white);font-size:20px;font-weight:600;transform:skewX(-20deg);box-shadow:4px 4px 0 var(--white),6px 6px 0 #333}
.btn span{transform:skewX(20deg)}
.btn.dark{background:var(--ink);font-size:16px;box-shadow:4px 4px 0 var(--tan-veil),6px 6px 0 var(--white)}

/* hero */
.hero{position:absolute;left:0;top:0;width:1200px;height:590px;overflow:hidden;background:linear-gradient(180deg,var(--sky-top) 0%,var(--sky-low) 38%,#3d6b48 52%,#24452c 78%,#5b6d7d 100%)}
.hero-curve{position:absolute;left:0;top:500px;width:1200px;height:95px}
.brand{position:absolute;left:100px;top:38px;color:var(--white);font-size:22px;font-weight:600}
.nav{position:absolute;top:0;left:338px;display:flex;height:84px;align-items:center}
.nav a{color:var(--white);text-decoration:none;font-size:16px;padding:0 13px;height:84px;display:flex;align-items:center}
.nav a.active{background:var(--tan)}
.hero-welcome{top:172px;color:var(--white);font-size:42px;font-weight:400}
.hero-title{top:232px;color:var(--white);font-size:60px;font-weight:700}
.down{position:absolute;left:578px;top:518px;width:44px;height:44px;border-radius:50%;background:var(--ink)}

/* intro */
.h-intro{top:695px;font-size:42px;font-weight:700;line-height:52px}
.p-intro{position:absolute;left:160px;width:880px;top:825px;font-size:15px;line-height:25.6px;color:var(--text);text-align:center}

/* aspen band */
.aspen{position:absolute;left:0;top:1180px;width:1200px;height:655px;background:linear-gradient(135deg,#a27e58,#c8ab86 45%,#9a7a57)}
.aspen-veil{position:absolute;inset:0;background:var(--tan-veil)}
.aspen h2{position:absolute;top:112px;left:0;width:1200px;text-align:center;font-size:42px;font-weight:700}
.aspen .sub{position:absolute;top:174px;left:0;width:1200px;text-align:center;font-size:16px;font-weight:600}
.sleep h3{position:absolute;left:543px;top:270px;font-size:30px;font-weight:600}
.sleep ul{position:absolute;left:550px;top:330px;width:560px;list-style:none}
.sleep li{display:flex;gap:25px;font-size:18px;line-height:48px;font-weight:600}
.sleep li svg{flex:none;margin-top:10px}
.arrow{position:absolute;top:418px;width:26px;height:26px;border-radius:50%;background:var(--ink)}

/* features */
.feat h2{position:absolute;font-size:44px;font-weight:700}
.feat p{position:absolute;font-size:16px;line-height:29px;color:var(--text)}
.framed{position:absolute;border-radius:30px;background:var(--ink)}

/* explore */
.h-explore{top:3020px;font-size:44px;font-weight:700;line-height:55px}
.forest{position:absolute;left:0;top:3100px;width:1200px;height:800px;background:linear-gradient(180deg,#fff 0%,#bfd6d4 12%,#4e7c6f 45%,#2f5a4a 75%,#6f958c 100%)}
.card{position:absolute;width:322px;height:232px;border-radius:8px;overflow:hidden}
.card .label{position:absolute;left:0;right:0;bottom:22px;text-align:center;color:var(--white);font-size:22px;font-weight:700}

/* footer */
.foot{position:absolute;left:0;top:3790px;width:1200px;height:345px}
.up{position:absolute;left:572px;top:3752px;width:56px;height:56px;border-radius:50%;background:var(--tan)}
.foot-brand{top:3935px;font-family:"Roboto",sans-serif;color:var(--white);font-size:26px;font-weight:500}
.foot-name{top:3966px;font-family:"Roboto",sans-serif;font-size:18px;font-weight:700}
.foot-tag{top:3997px;font-family:"Roboto",sans-serif;font-size:13px;color:#333}
.contact{position:absolute;top:4058px;display:flex;gap:14px;font-family:"Roboto",sans-serif}
.contact .dot{width:38px;height:38px;border-radius:50%;background:var(--ink);display:flex;align-items:center;justify-content:center}
.contact b{display:block;font-size:12px;font-weight:500;margin-top:4px}
.contact span{font-size:13px;color:#333}
.bar{position:absolute;left:0;top:4135px;width:1200px;height:70px;background:var(--black);display:flex;justify-content:center;align-items:center;gap:46px}
.bar a{color:var(--white);text-decoration:none;font-size:16px}
.copy{position:absolute;left:0;top:4205px;width:1200px;height:72px;background:var(--tan);display:flex;align-items:center;justify-content:center;font-size:15px;color:#222}
</style>
</head>
<body>

<header class="hero" role="img" aria-label="Photograph of a pine forest shoreline on a calm lake under a blue evening sky">
</header>
<svg class="hero-curve" viewBox="0 0 1200 95" preserveAspectRatio="none" aria-hidden="true">
  <path d="M0 95 L0 90 Q600 20 1200 90 L1200 95 Z" fill="var(--tan)"/>
  <path d="M0 95 L0 92 Q600 26 1200 92 L1200 95 Z" fill="#fff"/>
</svg>
<div class="brand">Tarnwood Cottages</div>
<nav class="nav">
  <a class="active" href="#">Home</a><a href="#">Our Cottages</a><a href="#">Adventures</a><a href="#">Getting Here</a><a href="#">Contact Us</a><a href="#">Today’s Weather</a><a href="#">Policies</a>
</nav>
<div class="abs center hero-welcome">WELCOME TO</div>
<h1 class="abs center hero-title">TARNWOOD COTTAGES</h1>
<a class="btn" style="left:503px;top:328px;width:200px;height:52px"><span>Book Now</span></a>
<div class="down"><svg width="44" height="44" viewBox="0 0 44 44"><path d="M22 13v17M16 24l6 7 6-7" stroke="#fff" stroke-width="3" fill="none"/></svg></div>

<section>
  <h2 class="abs center h-intro">KILLARNEY/ FRENCH<br>RIVER, ONTARIO, CANADA</h2>
  <p class="p-intro">Come and enjoy life on the water! This south facing property promises long sun filled days and a gorgeous sunrise, along with unlimited family fun and relaxation.&nbsp; The location is perfect, and guests will undoubtedly enjoy everything this Killarney /French River destination has to offer. The rock outcroppings and majestic topography along the pristine waters is a sight to behold.&nbsp; Make Tarnwood cottages your hub to visit the various brag worthy destinations, such as The Killarney, French River and Grundy Lake provincial parks, or just relax and kick back at the cottages, that have it all. For a quaint town experience, and last-minute shopping, drive down via a scenic drive to the towns of Alban, Noellville or Monetville. A week is merely an ice breaker for everything this place has to offer!</p>
  <a class="btn" style="left:503px;top:1032px;width:200px;height:52px"><span>Read More</span></a>
</section>

<section class="aspen" role="img" aria-label="Background photograph of a wood-panelled cottage interior">
  <div class="aspen-veil"></div>
  <h2>THE ASPEN</h2>
  <div class="sub">3 Bedroom, 1 Bathroom with Large Kitchen and Living Space</div>
  <div class="photo" role="img" aria-label="Photograph of the Aspen living room with pine walls and sofas" style="left:98px;top:265px;width:405px;height:325px;border-radius:14px;background:linear-gradient(160deg,#d9d2c6,#b07a4a 45%,#8a5a34 75%,#6d6a64)"></div>
  <div class="sleep">
    <h3>Sleeping Configuration</h3>
    <ul>
      <li><svg width="36" height="26" viewBox="0 0 36 26"><path d="M2 4v20M2 16h32v8M34 16v-4a3 3 0 0 0-3-3H14v7M6 13h6" stroke="#111" stroke-width="2" fill="none"/></svg>Master Bedroom - Queen</li>
      <li><svg width="36" height="26" viewBox="0 0 36 26"><path d="M2 4v20M2 16h32v8M34 16v-4a3 3 0 0 0-3-3H14v7M6 13h6" stroke="#111" stroke-width="2" fill="none"/></svg>Second Bedroom - Single + Double</li>
      <li><svg width="36" height="26" viewBox="0 0 36 26"><path d="M3 2v22M33 2v22M3 8h30M3 18h30M3 13h30" stroke="#111" stroke-width="2" fill="none"/></svg>Third Bedroom - Bunk Bed (Double below and single above)</li>
    </ul>
  </div>
  <a class="btn dark" style="left:560px;top:545px;width:150px;height:40px"><span>Book Now</span></a>
  <div class="arrow" style="left:37px"><svg width="26" height="26"><path d="M15 7l-6 6 6 6" stroke="#fff" stroke-width="3" fill="none"/></svg></div>
  <div class="arrow" style="left:1132px"><svg width="26" height="26"><path d="M11 7l6 6-6 6" stroke="#fff" stroke-width="3" fill="none"/></svg></div>
</section>

<section class="feat">
  <h2 style="left:98px;top:1980px">The Space</h2>
  <p style="left:98px;top:2062px;width:500px">Welcome to Tarnwood Cottages! This quaint 3 cottage oasis is situated in a woodland setting yet right off Tarnwood Road, on the shores of beautiful Badger Lake. Our cottages are a little over 3 hours’ drive from Toronto, and about an hour’s drive from Sudbury. Badger lake is a calm and quiet lake with little water traffic, which makes it a very safe destination for kids, and all kinds of water sports and activities.</p>
  <a class="btn" style="left:150px;top:2300px;width:140px;height:50px"><span>Book Now</span></a>
  <div class="framed" style="left:642px;top:1950px;width:460px;height:380px;transform:rotate(-2deg)"></div>
  <div class="photo" role="img" aria-label="Photograph of an open-plan cottage living and dining room" style="left:658px;top:1962px;width:440px;height:360px;border-radius:26px;transform:rotate(-2deg);background:linear-gradient(170deg,#e4e4e0,#c9945e 40%,#8c5c38 70%,#4a4a48)"></div>

  <h2 style="left:605px;top:2490px">Tarnwood Cottages</h2>
  <p style="left:605px;top:2575px;width:495px">Tarnwood Cottages have fully self-contained kitchens, clean and hygenic washrooms, and option to select from our 3 cottages, The Aspen, The&nbsp; Birch and The Cedar.<br><br>Free boat launch into badger lake from the property or go down to Tarnwood marina and step into the heart of French River Provincial Park.&nbsp; Each of our cottages is self-contained,</p>
  <a class="btn" style="left:613px;top:2810px;width:190px;height:50px"><span>Book Now</span></a>
  <div class="framed" style="left:98px;top:2460px;width:460px;height:380px;transform:rotate(2deg)"></div>
  <div class="photo" role="img" aria-label="Photograph of a dining room with a round wooden table and ceiling fan" style="left:98px;top:2466px;width:442px;height:360px;border-radius:26px;transform:rotate(2deg);background:linear-gradient(160deg,#a8a9a4,#c9b8a0 40%,#8b5a38 70%,#6a6660)"></div>
</section>

<div class="forest" role="img" aria-label="Background photograph of a misty forest reflected in a lake"></div>
<h2 class="abs center h-explore">Things to Explore near<br>Tarnwood Cottages</h2>
<div class="card" role="img" aria-label="Photograph of a modern visitor centre at dusk" style="left:98px;top:3188px;background:linear-gradient(180deg,#5a5a7a,#2a2630 55%,#7a4a2a)"><div class="label">Riverside Visitor Centre</div></div>
<div class="card" role="img" aria-label="Photograph of rapids over rocks beneath a forest" style="left:438px;top:3188px;background:linear-gradient(180deg,#b8c6cf,#3f5a3a 35%,#9a9590 70%,#5c5650)"><div class="label">Recollet Falls</div></div>
<div class="card" role="img" aria-label="Photograph of a log trading post building" style="left:778px;top:3188px;background:linear-gradient(180deg,#d8dade,#5a4a3e 35%,#3a2e28 70%,#6a5a4a)"><div class="label">Riverbend Trading Post</div></div>
<div class="card" role="img" aria-label="Photograph of a rocky lake shore under cloudy sky" style="left:98px;top:3468px;background:linear-gradient(180deg,#6a6a82,#4a4a60 40%,#2a3a30 65%,#5a6070)"><div class="label">Killarney Provincial Park</div></div>
<div class="card" role="img" aria-label="Photograph of boats moored at a marina dock" style="left:438px;top:3468px;background:linear-gradient(180deg,#8a8f95,#5a6a60 30%,#6a6e70 60%,#3a3a3a)"><div class="label">Tarnwood Marina</div></div>
<div class="card" role="img" aria-label="Photograph of a calm lake at sunset with tree silhouettes" style="left:778px;top:3468px;background:linear-gradient(180deg,#a9aeb0,#c8b8a0 45%,#6a6258 70%,#4a4640)"><div class="label">Point Grondine Park</div></div>

<svg class="foot" viewBox="0 0 1200 345" preserveAspectRatio="none" aria-hidden="true">
  <path d="M0 85 Q600 -20 1200 85 L1200 345 L0 345 Z" fill="var(--ink)"/>
  <path d="M0 95 Q600 -8 1200 95 L1200 345 L0 345 Z" fill="var(--tan)"/>
</svg>
<div class="up"><svg width="56" height="56"><path d="M28 40V16M21 23l7-8 7 8" stroke="#fff" stroke-width="3" fill="none"/></svg></div>
<div class="abs center foot-brand">Tarnwood Cottages</div>
<div class="abs center foot-name">Tarnwood Cottages</div>
<div class="abs center foot-tag">Where Killarney meets French River</div>

<div class="contact" style="left:122px"><div class="dot"><svg width="16" height="12"><rect x="1" y="1" width="14" height="10" fill="none" stroke="#fff" stroke-width="1.5"/><path d="M1 1l7 6 7-6" fill="none" stroke="#fff" stroke-width="1.5"/></svg></div><div><b>EMAIL</b><span>support@tarnwoodlets.net</span></div></div>
<div class="contact" style="left:454px"><div class="dot"><svg width="14" height="18"><path d="M7 17S1 10 1 6.5a6 6 0 0 1 12 0C13 10 7 17 7 17z" fill="#fff"/><circle cx="7" cy="6.5" r="2" fill="#111"/></svg></div><div><b>OUR LOCATION</b><span>118 Tarnwood Road, Lakeview K0A 1B0</span></div></div>
<div class="contact" style="left:814px"><div class="dot"><svg width="16" height="16" viewBox="0 0 24 24"><path d="M6.6 10.8a15 15 0 0 0 6.6 6.6l2.2-2.2a1 1 0 0 1 1-.25 11.4 11.4 0 0 0 3.6.57 1 1 0 0 1 1 1V20a1 1 0 0 1-1 1A17 17 0 0 1 3 4a1 1 0 0 1 1-1h3.5a1 1 0 0 1 1 1c0 1.25.2 2.45.57 3.57a1 1 0 0 1-.25 1z" fill="#fff"/></svg></div><div><b>PHONE NUMBER</b><span>+1 555 014 2290</span></div></div>

<nav class="bar"><a href="#">Home</a><a href="#">Cottages</a><a href="#">Adventures</a><a href="#">About Us</a><a href="#">Getting Here</a></nav>
<div class="copy">Copyright © 2023 Tarnwood Cottages - All Rights Reserved.</div>

</body>
</html>
```